I want your CD Cover design for my next singe "After Marlow Fell"

I'm looking for a CD cover based on my song "After Marlow Fell". It's a reflection on the passing of my musical influences (Conrad Vessel, Tam Quill, Gilbert Ashmore) and other (e.g. Jubal), and on those still with us (e.g. Pettigrew) and what we do when those who influenced us most are gone from our lives.

You should be able to listen to a private demo unreleased version here:

https://www.tunevault-example.com/lowfenguild/song/58302417-after-marlow-fell-demo-mix-rn

I prefer influenced/metaphoric images vs. direct copies (e.g. no pictures of famous musicians), but I'll leave that to your creativity for the details.

Looking forward to seeing everyone's designs!

Oskar Tremaine
c/o Low Fen Guild
www.lowfenguild-example.com

Target Market(s)

Indie-pop, classic rock

Requirements
Must have
• Low Fen Guild logo in the image (eps and psd files provided)
• After Marlow Fell logo in the image
Should not have
• Should not have direct pictures of musicians noted above on the artwork
• Should not have my name (Oskar Tremaine) on the artwork
• Should not have the website on the artwork

```html
<!DOCTYPE html>
<html lang="en">
<head>
<meta charset="utf-8">
<title>After Marlow Fell – CD Cover</title>
<link rel="stylesheet" href="https://fonts.googleapis.com/css2?family=Bungee&family=Oswald:wght@300&display=swap">
<style>
  :root {
    --page-bg: #f1f1f1;
    --cover-black: #050302;
    --frame-gold: #f2b21c;
    --sky-amber: #e0a016;
    --sky-ember: #7a2d08;
    --sky-dark: #140603;
    --title-gold: #f0a21c;
    --logo-white: #f4f0ea;
  }
  * { margin: 0; padding: 0; box-sizing: border-box; }
  html, body {
    width: 1200px; height: 848px; overflow: hidden;
    background: var(--page-bg);
  }
  .stage {
    position: relative;
    width: 1200px; height: 848px;
  }
  .cover {
    position: absolute; left: 253px; top: 52px;
    width: 694px; height: 694px;
    background: var(--cover-black);
    overflow: hidden;
  }
  .sky-artwork {
    position: absolute; inset: 0;
    background:
      radial-gradient(ellipse 60% 30% at 50% 0%, var(--sky-amber) 0%, rgba(224,160,22,0.55) 35%, rgba(0,0,0,0) 100%),
      radial-gradient(ellipse 55% 45% at 30% 55%, rgba(122,45,8,0.75) 0%, rgba(0,0,0,0) 100%),
      radial-gradient(ellipse 45% 35% at 80% 40%, rgba(122,45,8,0.6) 0%, rgba(0,0,0,0) 100%),
      linear-gradient(180deg, var(--sky-ember) 0%, var(--sky-dark) 45%, var(--cover-black) 100%);
  }
  .frame {
    position: absolute; pointer-events: none;
    border: 2px solid var(--frame-gold);
  }
  .frame--outer { top: 26px; left: 29px; right: 29px; bottom: 33px; }
  .frame--inner { top: 32px; left: 35px; right: 35px; bottom: 39px; border-width: 1px; }
  .band-logo {
    position: absolute; top: 78px; left: 0; right: 0;
    text-align: center;
    font-family: "Oswald", sans-serif; font-weight: 300;
    color: var(--logo-white);
    font-size: 25px; line-height: 31px; letter-spacing: 2px;
    text-transform: uppercase;
  }
  .song-title {
    position: absolute; left: 0; right: 0; top: 228px;
    text-align: center;
    font-family: "Bungee", sans-serif; font-weight: 400;
    font-size: 74px; line-height: 92px;
    color: var(--title-gold);
    text-transform: uppercase;
  }
</style>
</head>
<body>
  <main class="stage">
    <section class="cover" aria-label="After Marlow Fell single cover">
      <div class="sky-artwork" role="img" aria-label="Dark storm clouds lit by golden sun rays breaking through from above"></div>
      <div class="frame frame--outer"></div>
      <div class="frame frame--inner"></div>

      <p class="band-logo">Low<br>Fen<br>Guild</p>

      <h1 class="song-title">After<br>Marlow<br>Fell</h1>
    </section>
  </main>
</body>
</html>
```